2 Page Brochure Design Project

I have attached a 2 page word document. I want this document made into a more professional and quality looking document. The colours / look and feel must be in line with a .pdf document I have attached.
I do not have the raw image files from the attached word document and realise that in the designed brochure, they resolution will be poor. Just use what I have provided and I will add my own pictures as layer in substitute for these ones later on myself.
Target Market(s)
Mining Sector
Industry/Entity Type
It Professional
Requirements
Must have
- 1. Must have same look and feel as attached .pdf. It does not need the black and white truck, but must be similar in effects.
2. Must be created in Photoshop (other packages not acceptable).
3. All source files including any 3rd party images must be provided by the successful designer.
4. Although the photo's are different sizes in the attached word document, I would prefer them to be the same size in the brochure, but this is not essential.
5. A4 size for each page
6. High Res as this will be printed. I can make it lower quality for web publishing later.

```html
<!DOCTYPE html>
<html lang="en">
<head>
<meta charset="utf-8">
<title>Pit Marks – ID Label Fitment Guide</title>
<link href="https://fonts.googleapis.com/css2?family=Exo+2:wght@300;400;600;800&family=Fira+Sans:ital,wght@0,400;0,500;1,500&display=swap" rel="stylesheet">
<style>
  :root {
    --yellow: #f4e01c;
    --yellow-band: rgba(244, 224, 28, 0.86);
    --black-band: rgba(18, 18, 18, 0.86);
    --ink: #161616;
    --white: #ffffff;
    --gold-text: #d9c63a;
    --sky-top: #2c6db3;
    --sky-low: #b9d3ea;
    --dirt-top: #c98c3c;
    --dirt-low: #7d3f1c;
  }
  * { margin: 0; padding: 0; box-sizing: border-box; }
  html, body { width: 1200px; height: 900px; overflow: hidden; background: var(--white); }
  body { position: relative; font-family: "Fira Sans", sans-serif; color: var(--ink); }

  .spread-photo {
    position: absolute; left: 30px; top: 174px; width: 1140px; height: 686px;
    background: linear-gradient(180deg, var(--sky-top) 0%, var(--sky-low) 30%, var(--dirt-top) 42%, #b06a2c 70%, var(--dirt-low) 100%);
  }

  .brand { position: absolute; display: flex; align-items: center; gap: 12px;
    font-family: "Exo 2", sans-serif; font-weight: 800; color: var(--ink); letter-spacing: 1px; }
  .brand-mark { background: var(--yellow); display: block; }
  .brand--cover { left: 44px; top: 84px; font-size: 46px; }
  .brand--cover .brand-mark { width: 44px; height: 44px; }
  .brand--inner { left: 622px; top: 96px; font-size: 28px; }
  .brand--inner .brand-mark { width: 28px; height: 28px; }

  .contact { position: absolute; right: 613px; top: 68px; text-align: right;
    font-family: "Exo 2", sans-serif; font-size: 10.5px; line-height: 13.8px; font-weight: 600; }

  .inner-title { position: absolute; left: 888px; top: 92px; font-family: "Exo 2", sans-serif; }
  .inner-title h1 { font-size: 31px; font-weight: 400; letter-spacing: 0.5px; line-height: 1; }
  .inner-title p { font-size: 17px; color: var(--gold-text); margin-top: 4px; }

  .guide-bar { position: absolute; left: 30px; top: 174px; width: 573px; height: 38px;
    background: var(--yellow); display: flex; align-items: center; justify-content: space-between; padding: 0 18px 0 26px; }
  .guide-bar h2 { font-family: "Exo 2", sans-serif; font-weight: 400; font-size: 17px; }
  .guide-bar p { font-family: "Exo 2", sans-serif; font-size: 7.5px; font-weight: 600; width: 200px; line-height: 11px; }

  .photo { border: 3px solid var(--white); position: absolute; }
  .items-photo { left: 68px; top: 236px; width: 112px; height: 112px;
    background: linear-gradient(135deg, #c4c4c4, #7d8690 60%, #3a4e8c); }
  .items { position: absolute; left: 202px; top: 242px; color: var(--white); font-family: "Exo 2", sans-serif; font-size: 11px; line-height: 14px; }
  .items h3 { font-weight: 400; font-size: 12px; margin-bottom: 2px; }
  .items ol { padding-left: 14px; }
  .cover-heading { position: absolute; left: 162px; top: 362px; color: var(--white);
    font-family: "Exo 2", sans-serif; font-weight: 300; font-size: 38px; }

  .step { position: absolute; width: 567px; display: flex; align-items: center; }
  .step--left { left: 30px; width: 573px; }
  .step--right { left: 603px; }
  .step--dark { background: var(--black-band); color: var(--white); }
  .step--light { background: var(--yellow-band); color: var(--ink); }
  .step-number { font-family: "Exo 2", sans-serif; font-size: 40px; font-weight: 400; width: 94px; padding-left: 16px; letter-spacing: 1px; }
  .step-photo { position: relative; width: 78px; height: 78px; border: 3px solid var(--white); flex: none;
    background: linear-gradient(135deg, #d8d8d8, #8a8a8a); }
  .step-photo--label { background: linear-gradient(135deg, #3a3a3a, #1a1a1a 60%, #b8b23a); }
  .step-text { margin-left: 46px; width: 322px; font-size: 11.5px; line-height: 15.5px; }
  .step-text .note { display: block; font-style: italic; font-size: 8.5px; line-height: 11px; }
  .step--bold .step-text { font-weight: 500; }
</style>
</head>
<body>
  <div class="spread-photo" role="img" aria-label="Wide photograph of a haul truck on a mine site under a blue sky, spanning both pages"></div>

  <div class="brand brand--cover"><span class="brand-mark"></span>PIT MARKS</div>
  <address class="contact">
    PIT MARKS<br>ABN: 51 204 118 302<br>Unit 4, 18-20 Ridgeway Street<br>KINGSFORD&nbsp; QLD&nbsp; 4130<br>PHONE: 07 3100 2481<br>FAX: 07 3100 2482<br>EMAIL:info@pitmarks.com.au
  </address>

  <div class="brand brand--inner"><span class="brand-mark"></span>PIT MARKS</div>
  <div class="inner-title">
    <h1>APPLICATION STEPS</h1>
    <p>PIT MARKS ID LABEL FITMENT GUIDE</p>
  </div>

  <div class="guide-bar">
    <h2>PIT MARKS ID LABEL FITMENT GUIDE</h2>
    <p>A CLEAN SURFACE IS KEY TO FULL ADHESION FOR LONG SERVICE LIFE OF THE ID LABEL</p>
  </div>

  <div class="photo items-photo" role="img" aria-label="Photo of cleaning tin, tape measure, scissors, squeegee and masking tape"></div>
  <div class="items">
    <h3>ITEMS REQUIRED –</h3>
    <ol>
      <li>Quick drying evaporative cleaning product such as Quikprep.</li>
      <li>Clean rags to clean surface</li>
      <li>Masking tape [50mm]</li>
      <li>Scissors</li>
      <li>Squeegee</li>
      <li>Tape Measure</li>
    </ol>
  </div>
  <div class="cover-heading">APPLICATION STEPS</div>

  <!-- Left page steps -->
  <div class="step step--left step--dark" style="top:411px;height:104px;">
    <div class="step-number">01.</div>
    <div class="step-photo" role="img" aria-label="Photo of surface being cleaned with a rag"></div>
    <p class="step-text">Use Quikprep and rags to thoroughly clean surface.</p>
  </div>
  <div class="step step--left step--light" style="top:524px;height:94px;">
    <div class="step-number">02.</div>
    <div class="step-photo" role="img" aria-label="Photo of measuring tape marking label position"></div>
    <p class="step-text">Use measuring tape to mark label position.</p>
  </div>
  <div class="step step--left step--dark" style="top:626px;height:114px;">
    <div class="step-number">03.</div>
    <div class="step-photo" role="img" aria-label="Photo of label taped in position"></div>
    <p class="step-text">Position sign without removing the backing paper and use a tab of masking tape at each side on the vertical edge to hold the ID Label in position.</p>
  </div>
  <div class="step step--left step--light" style="top:752px;height:98px;">
    <div class="step-number">04.</div>
    <div class="step-photo step-photo--label" role="img" aria-label="Photo of ID label with vertical masking tape strip"></div>
    <p class="step-text">When you are happy with the position of the ID label, place a strip of masking tape vertically across the full length of the ID Label just past centre to ensure the label doesn't move.</p>
  </div>

  <!-- Right page steps -->
  <div class="step step--right step--dark" style="top:183px;height:104px;">
    <div class="step-number">05.</div>
    <div class="step-photo" role="img" aria-label="Photo of sticker folded back halfway"></div>
    <p class="step-text">Cut the masking tape tab on the right side edge of the sticker so you can fold the sticker back toward you half way.</p>
  </div>
  <div class="step step--right step--light step--bold" style="top:296px;height:102px;">
    <div class="step-number">06.</div>
    <div class="step-photo" role="img" aria-label="Photo of backing paper being peeled off"></div>
    <p class="step-text">Peel the backing paper off the label, cutting the excess paper off with your scissors.</p>
  </div>
  <div class="step step--right step--dark" style="top:411px;height:102px;">
    <div class="step-number">07.</div>
    <div class="step-photo step-photo--label" role="img" aria-label="Photo of label laid back on the surface"></div>
    <p class="step-text">Lay the label back on to the surface carefully realigning your masking tape to ensure your label is straight.</p>
  </div>
  <div class="step step--right step--light step--bold" style="top:525px;height:95px;">
    <div class="step-number">08.</div>
    <div class="step-photo step-photo--label" role="img" aria-label="Photo of label being squeegeed from the centre out"></div>
    <p class="step-text">Holding the right hand edge of the label off the surface, use your squeegee and start rubbing the surface using a centre out motion toward the right hand edge.<span class="note">**Holding the right hand edge of the label off the surface,&nbsp; this ensures that as you squeegee out, it releases any air bubbles from getting trapped**</span></p>
  </div>
  <div class="step step--right step--dark" style="top:630px;height:110px;">
    <div class="step-number">09.</div>
    <div class="step-photo step-photo--label" role="img" aria-label="Photo of centre masking strip being removed"></div>
    <p class="step-text">Remove the centre strip of masking tape and repeat steps 3 through 7 only this time on the left hand side of the ID Label</p>
  </div>
  <div class="step step--right step--light step--bold" style="top:752px;height:98px;">
    <div class="step-number">10.</div>
    <div class="step-photo" role="img" aria-label="Photo of squeegee pressing label edges"></div>
    <p class="step-text">Remove all excess masking tape and squeegee the outside edges ensuring full adhesion contact is made.</p>
  </div>
</body>
</html>
```